依頼詳細
商品は布マスクになりますが、取り急ぎ添付の不織布マスクの内容で構いせん。
全体のイメージで決定したいと思います。
決定後に布マスクの詳細をお伝えしますので、完成品に仕上げて頂きたいと思います。

製品形状はPP袋(PPのベースは透明もしくはアルミ銀)
袋サイズ:W130xH180mm+ヘッダー部分H20mm

印刷は4色分解でも構いませんが、中国印刷の為、あまり複雑過ぎない程度の色使いでお願いします。

急ぎ提案なのでイメージだけでも早く提案してもらえば助かります。
説明不足で申し訳ございませんが、不明点はご連絡お願い致します。
記載項目
PP袋(PPのベースは透明もしくはアルミ銀)

印刷は4色分解でも構いませんが、中国グラビア印刷(8色まで)の為、あまり複雑過ぎない程度の色使いでお願いします。版代のコストも抑えたいです。
希望イメージ
シンプル 複雑
単色 カラフル
暗い 明るい
日常 高級
遊び心 厳粛
未来的 伝統的
女性的 男性的
希望する色
青系、水色系、無彩色系
納品ファイル
• イラストレーター形式 (.ai)
補足説明

お客様の選定により

たくさんのご提案ありがとうございました
またの機会にも是非またご提案お願い致します。

```html
<!DOCTYPE html>
<html lang="ja">
<head>
<meta charset="UTF-8">
<title>布マスク パッケージ</title>
<link rel="stylesheet" href="https://fonts.googleapis.com/css2?family=Noto+Sans+JP:wght@400;700;900&display=swap">
<style>
  :root {
    --sky: #bfe2f4;
    --sky-deep: #8fcbea;
    --blue: #1f8fd6;
    --navy: #15579a;
    --white: #ffffff;
    --mask-tone: #eef6fb;
  }
  * { margin: 0; padding: 0; box-sizing: border-box; }
  html, body { width: 882px; height: 1200px; overflow: hidden; background: var(--white); }
  body { font-family: "Noto Sans JP", sans-serif; }
  .package {
    position: relative; width: 882px; height: 1200px;
    background: linear-gradient(180deg, var(--sky) 0%, #d7eefa 75%);
    overflow: hidden;
  }
  .origin-badge {
    position: absolute; left: 30px; top: 25px; width: 150px; height: 58px;
    background: var(--white); border: 4px solid var(--blue);
    color: var(--blue); font-weight: 900; font-size: 38px;
    display: flex; align-items: center; justify-content: center; letter-spacing: 2px;
  }
  .origin-en { position: absolute; left: 195px; top: 55px; color: var(--navy); font-size: 20px; font-weight: 700; }
  .size-badge { position: absolute; right: 28px; top: 25px; width: 200px; text-align: center; }
  .size-badge .grade {
    background: var(--white); border: 3px solid var(--blue); color: var(--navy);
    font-size: 30px; font-weight: 700; height: 50px; line-height: 44px;
  }
  .size-badge .dims { background: var(--blue); color: var(--white); font-size: 20px; height: 32px; line-height: 32px; }
  .wash-banner {
    position: absolute; left: 205px; top: 108px; width: 490px; height: 46px;
    background: var(--white); border-radius: 23px; color: var(--navy);
    font-size: 30px; font-weight: 900; text-align: center; line-height: 46px;
  }
  .cloth-block {
    position: absolute; left: 70px; top: 165px; width: 215px; height: 185px;
    background: var(--blue); color: var(--white); font-size: 175px; font-weight: 900;
    display: flex; align-items: center; justify-content: center; line-height: 1;
  }
  .product-name {
    position: absolute; left: 300px; top: 150px; color: var(--blue);
    font-size: 150px; font-weight: 900; line-height: 1.1; letter-spacing: 4px;
  }
  .guard-icons { position: absolute; left: 395px; top: 318px; display: flex; gap: 12px; }
  .guard-icons li {
    list-style: none; width: 86px; height: 86px; border-radius: 50%;
    background: var(--blue); color: var(--white); font-size: 17px; font-weight: 700;
    display: flex; align-items: center; justify-content: center; text-align: center; line-height: 1.2;
  }
  .mask-visual {
    position: absolute; left: 60px; top: 420px; width: 780px; height: 430px;
    background: radial-gradient(ellipse at 55% 55%, var(--white) 0%, var(--mask-tone) 55%, var(--sky) 100%);
    border-radius: 40px;
  }
  .filter-label {
    position: absolute; left: 20px; top: 440px; background: var(--blue); color: var(--white);
    font-size: 24px; font-weight: 700; padding: 6px 18px;
  }
  .fit-note { position: absolute; left: 560px; top: 460px; color: var(--navy); font-size: 17px; line-height: 1.4; }
  .footnote { position: absolute; left: 40px; top: 862px; color: var(--navy); font-size: 15px; line-height: 1.5; }
  .claim-panel { position: absolute; left: 0; top: 915px; width: 882px; height: 285px; background: var(--white); }
  .percent-num {
    position: absolute; left: 36px; top: 918px; color: var(--blue);
    font-weight: 900; font-size: 240px; line-height: 1; letter-spacing: -8px;
  }
  .percent-sign {
    position: absolute; left: 302px; top: 1085px; color: var(--blue);
    font-weight: 900; font-size: 76px; line-height: 1;
  }
  .claim-title {
    position: absolute; left: 385px; top: 965px; color: var(--blue);
    font-size: 58px; font-weight: 900; line-height: 1.1; white-space: nowrap;
  }
  .claim-band {
    position: absolute; left: 385px; top: 1060px; width: 470px; height: 60px;
    background: var(--blue); color: var(--white); font-size: 34px; font-weight: 700;
    text-align: center; line-height: 60px; white-space: nowrap;
  }
</style>
</head>
<body>
<main class="package">
  <div class="origin-badge">日本製</div>
  <div class="origin-en">Made in JAPAN</div>
  <div class="size-badge">
    <div class="grade">ふつう</div>
    <div class="dims">約17.5cm×9.5cm</div>
  </div>
  <div class="wash-banner">繰り返し洗って使える</div>
  <div class="cloth-block">布</div>
  <h1 class="product-name">マスク</h1>
  <ul class="guard-icons">
    <li>花粉</li>
    <li>ウィルス<br>飛沫</li>
    <li>ハウス<br>ダスト</li>
    <li>PM2.5</li>
  </ul>
  <div class="mask-visual" role="img" aria-label="白いプリーツマスクと3層フィルターの図"></div>
  <div class="filter-label">3層フィルター採用</div>
  <p class="fit-note">ノーズフィットで<br>ぴったりフィット。</p>
  <p class="footnote">※フィルターの捕集効率試験による<br>※花粉・ウィルス飛沫・PM2.5を約99%カット</p>
  <div class="claim-panel"></div>
  <div class="percent-num">99</div>
  <div class="percent-sign">%</div>
  <div class="claim-title">ウィルス カット!</div>
  <div class="claim-band">カットフィルター使用</div>
</main>
</body>
</html>
```